Kelvo Marine business card

We sell live saltwater fish and live corals
Kelvo Marine
7 Harlow Ct
Dunmere, NJ. 08099
(856) 555-0147
Contact Information for Business Card
Kelvo Marine
7 Harlow Ct
Dunmere, NJ. 08099
(856) 555-0147
Colors
Designer to choose colors to be used in the design.

```html
<!DOCTYPE html>
<html lang="en">
<head>
<meta charset="utf-8">
<title>Kelvo Marine — Business Card</title>
<link rel="stylesheet" href="https://fonts.googleapis.com/css2?family=Lato:wght@400;700&display=swap">
<style>
  :root {
    --backdrop: #e6e3df;
    --card-dark: #333335;
    --card-light: #ffffff;
    --ink-light: #ffffff;
    --ink-dark: #2b2b2d;
    --ink-muted: #707070;
    --rule: #2b2b2d;
  }
  * { margin: 0; padding: 0; box-sizing: border-box; }
  html, body {
    width: 1200px;
    height: 848px;
    overflow: hidden;
    background: var(--backdrop);
    font-family: "Lato", Arial, sans-serif;
  }
  .canvas {
    position: relative;
    width: 1200px;
    height: 848px;
  }
  .card {
    position: absolute;
    left: 251px;
    width: 674px;
    height: 378px;
  }
  .card--front {
    top: 28px;
    background: var(--card-dark);
    display: flex;
    align-items: center;
    justify-content: center;
  }
  .front-title {
    color: var(--ink-light);
    font-weight: 700;
    font-size: 64px;
    line-height: 1;
    letter-spacing: 0.3px;
    margin-top: -8px;
  }
  .card--back {
    top: 441px;
    background: var(--card-light);
  }
  .back-name {
    position: absolute;
    right: 360px;
    top: 173px;
    color: var(--ink-dark);
    font-weight: 700;
    font-size: 22px;
    line-height: 26px;
    white-space: nowrap;
  }
  .back-rule {
    position: absolute;
    left: 336px;
    top: 148px;
    width: 1px;
    height: 78px;
    background: var(--rule);
  }
  .back-details {
    position: absolute;
    left: 360px;
    top: 145px;
    color: var(--ink-muted);
    font-size: 18px;
    font-style: normal;
    line-height: 23px;
    white-space: nowrap;
  }
  .back-phone {
    margin-top: 16px;
    display: flex;
    align-items: center;
    gap: 6px;
  }
  .back-phone svg { width: 12px; height: 14px; }
</style>
</head>
<body>
<main class="canvas">
  <section class="card card--front">
    <h1 class="front-title">KELVO MARINE</h1>
  </section>
  <section class="card card--back">
    <p class="back-name">Kelvo Marine</p>
    <div class="back-rule"></div>
    <address class="back-details">
      <div>7 Harlow Ct</div>
      <div>Dunmere, NJ. 08099</div>
      <div class="back-phone">
        <svg viewBox="0 0 12 14" aria-hidden="true">
          <path d="M2.6 0.6 L4.6 3.4 C4.8 3.8 4.7 4.2 4.4 4.5 L3.6 5.2 C4.3 7.2 5.3 8.8 6.9 10 L7.8 9.4 C8.1 9.2 8.6 9.2 8.9 9.5 L10.9 11.7 C11.2 12 11.1 12.5 10.8 12.8 L9.8 13.4 C8.9 13.9 7.7 13.7 6.6 13 C3.6 10.9 1.3 7.4 0.6 3.8 C0.4 2.6 0.7 1.5 1.6 0.8 L2.1 0.5 C2.3 0.4 2.5 0.4 2.6 0.6 Z" fill="var(--ink-dark)"/>
        </svg>
        <span>(856) 555-0147</span>
      </div>
    </address>
  </section>
</main>
</body>
</html>
```